One-of-a-kind graphic design that is classy and simplistic, but, WOWS!

We need a graphic design for a new product called OVeRANT®. A product that shows what famous people one may be like just by using their name and birth date. The end product is a one-page graphic representation showcasing the qualities, similarities, and actual likenesses of those results. As stated, our desire is to make this into a "one-of-a-kind graphic design that is classy and simplistic, but, WOWS!"

Would like the wording and format to remain the same and an awesome background be designed that enhances the information. The background needs to be simple, classy, and elegant in a style that makes people go "WOW!" Something one-of-a-kind. Something so damn good people will say, "I gotta get one of those!"

Final graphic has to be provided in a .psd of the same size and every aspect (layer) needs to be fully editable. Information must be able to be updated and changed without having issue with the overall design. One main thing is: the words "AM" "i" and "LIKE" in the graphic must be able to "fade" as much as desired. Meaning: those words in the graphic can be modified as light or as dark as we need to make them.

Target Market(s)

Greeting Card market overall, but, specifically, Gen Y and Gen Z

Requirements
Must have
• Must have the original wording and formatted size, but, can be "enhanced" in any way.
Nice to have
• Like to see an incorporation of something related to Sacred Geometry but not taking over the design. The background has to enhance the wording. If that makes sense? Something that would work as a wall hanging in someone's home, for the Carvelo crowd as well as Bop-Lum'ers.

```html
<!DOCTYPE html>
<html lang="en">
<head>
<meta charset="utf-8">
<title>OVeRANT — Who Am I</title>
<link rel="stylesheet" href="https://fonts.googleapis.com/css2?family=Jost:wght@400;500;600;700;800&family=Open+Sans:wght@400;600&display=swap">
<style>
  :root {
    --paper: #e8e8ea;
    --ink: #2c2233;
    --ink-dark: #1c1820;
    --ghost-grey: #cbcacc;
    --ghost-light: #f1f0f2;
    --white: #ffffff;
    --violet-top: #5d5580;
    --violet-mid: #5e4a6e;
    --plum-bottom: #7c4c69;
    --panel: rgba(255, 255, 255, 0.12);
    --pillar: rgba(255, 255, 255, 0.2);
  }
  * { margin: 0; padding: 0; box-sizing: border-box; }
  html, body { width: 748px; height: 1200px; overflow: hidden; background: var(--white); }
  .canvas { position: relative; width: 748px; height: 1200px; overflow: hidden; font-family: "Jost", sans-serif; color: var(--ink); }

  /* Intro band */
  .intro { position: absolute; left: 0; top: 0; width: 748px; height: 382px; background: var(--paper); overflow: hidden; }
  .intro-ghost, .numeral, .like-ghost { position: absolute; left: 0; top: 0; }
  .intro-title { position: absolute; left: 0; width: 870px; top: 55px; text-align: center; font-weight: 800; font-size: 15.5px; letter-spacing: 0.3px; color: var(--ink-dark); }
  .intro-copy { position: absolute; left: 0; top: 0; width: 748px; font-size: 13.4px; font-weight: 500; color: var(--ink-dark); }
  .intro-copy .line { position: absolute; right: 52px; text-align: justify; text-align-last: justify; white-space: nowrap; line-height: 1; }
  .intro-copy .line.last { text-align: left; text-align-last: left; right: auto; }

  /* Profile band */
  .profile { position: absolute; left: 0; top: 382px; width: 748px; height: 405px; overflow: hidden; }
  .profile-backdrop { position: absolute; inset: 0;
    background:
      radial-gradient(ellipse at 50% 45%, rgba(150, 110, 150, 0.25), transparent 60%),
      linear-gradient(180deg, var(--violet-top) 0%, var(--violet-mid) 55%, var(--plum-bottom) 100%); }
  .pillar { position: absolute; left: 36px; top: 63px; width: 77px; height: 279px; background: var(--pillar); }
  .person-name { position: absolute; left: 132px; top: 77px; font-size: 23.5px; font-weight: 500; color: var(--white); letter-spacing: 0.2px; }
  .person-date { position: absolute; left: 132px; top: 117px; font-family: "Open Sans", sans-serif; font-size: 17px; color: var(--white); }
  .trait { position: absolute; left: 371px; width: 267px; height: 63px; background: var(--panel); }
  .trait svg { position: absolute; left: 15px; top: 18px; }
  .trait-label { position: absolute; left: 59px; top: 12px; font-size: 13px; font-weight: 600; color: var(--white); letter-spacing: 0.2px; }
  .trait-value { position: absolute; left: 59px; top: 33px; font-family: "Open Sans", sans-serif; font-size: 15.5px; color: var(--white); }
  .brand-line { position: absolute; left: 56px; bottom: -9px; font-size: 42px; font-weight: 500; color: var(--white); letter-spacing: 0.5px; line-height: 1; }

  /* Likeness list */
  .likeness { position: absolute; left: 0; top: 787px; width: 748px; height: 413px; background: var(--white); }
  .marker-left { position: absolute; left: 0; top: 83px; width: 29px; height: 26px; background: var(--ink-dark); }
  .marker-right { position: absolute; left: 718px; top: 314px; width: 27px; height: 99px; background: var(--ink-dark); }
  .match-list { position: absolute; top: 80px; list-style: none; }
  .match-list li { position: relative; height: 31.2px; padding-left: 23px; font-size: 12.2px; font-weight: 700; letter-spacing: 0.2px; color: var(--ink); line-height: 18px; }
  .match-list li svg { position: absolute; left: 0; top: 4px; }
  .col-a { left: 73px; } .col-b { left: 296px; } .col-c { left: 513px; }
</style>
</head>
<body>
<div class="canvas">

  <section class="intro">
    <svg class="intro-ghost" width="748" height="382" aria-hidden="true">
      <text x="192" y="372" textLength="541" lengthAdjust="spacingAndGlyphs" font-family="Jost, sans-serif" font-weight="800" font-size="306" fill="var(--ghost-grey)">AM</text>
    </svg>
    <svg class="numeral" width="160" height="310" aria-label="1" role="img">
      <path d="M44.5 101.4 H146.4 V298.8 H75.2 V165.2 L44.5 167.2 Z" fill="var(--ink)"/>
    </svg>
    <h1 class="intro-title">WHO AM I...</h1>
    <div class="intro-copy">
      <span class="line" style="left:183px;top:96px">Each Overant is formatted to showcase the individual qualities one possesses if they</span>
      <span class="line" style="left:195.5px;top:120px">are that number. An overall outlook is given of those traits along with a</span>
      <span class="line" style="left:208px;top:144px">breakdown of the positive and negative attributes of the number, culminating</span>
      <span class="line" style="left:220.5px;top:169px">in a final takeaway for those who are this particular number. Basically, the</span>
      <span class="line" style="left:233.5px;top:193px">meaning of this number, what an individual expresses if they are this</span>
      <span class="line" style="left:246.5px;top:217px">number, their personal tendencies, all displayed with positive outlooks</span>
      <span class="line" style="left:258.5px;top:241px">first, followed by negative traits culminating in a final lesson for those</span>
      <span class="line" style="left:271.5px;top:266px">possessing the traits of this number. It all comes together to show</span>
      <span class="line last" style="left:284.5px;top:290px">what you are like before revealing WHO you are like...</span>
    </div>
  </section>

  <section class="profile">
    <div class="profile-backdrop" role="img" aria-label="Soft violet-to-plum backdrop with a faint sacred geometry flower-of-life pattern"></div>
    <div class="pillar"></div>
    <h2 class="person-name">JANE STARDOM</h2>
    <p class="person-date">07.07.1977</p>

    <div class="trait" style="top:65px">
      <svg width="27" height="27" aria-hidden="true"><circle cx="13.5" cy="13.5" r="13" fill="var(--white)"/><path d="M7.5 13.8 L11.8 18 L19.5 9.5" stroke="var(--violet-mid)" stroke-width="3.2" fill="none" stroke-linecap="round" stroke-linejoin="round"/></svg>
      <div class="trait-label">OVERALL TRAIT:</div>
      <div class="trait-value">Independent</div>
    </div>
    <div class="trait" style="top:133.5px">
      <svg width="27" height="27" aria-hidden="true"><circle cx="13.5" cy="13.5" r="13" fill="var(--white)"/><path d="M7.5 13.8 L11.8 18 L19.5 9.5" stroke="var(--violet-mid)" stroke-width="3.2" fill="none" stroke-linecap="round" stroke-linejoin="round"/></svg>
      <div class="trait-label">POSITIVE TRAIT:</div>
      <div class="trait-value">Self-sufficient</div>
    </div>
    <div class="trait" style="top:204px">
      <svg width="27" height="27" aria-hidden="true"><circle cx="13.5" cy="13.5" r="13" fill="var(--white)"/><path d="M7.5 13.8 L11.8 18 L19.5 9.5" stroke="var(--violet-mid)" stroke-width="3.2" fill="none" stroke-linecap="round" stroke-linejoin="round"/></svg>
      <div class="trait-label">NEGATIVE TRAIT:</div>
      <div class="trait-value">Dependent/Selfish</div>
    </div>

    <div class="brand-line">OVeRANT...</div>
  </section>

  <section class="likeness">
    <svg class="like-ghost" width="748" height="200" aria-hidden="true">
      <text x="110" y="189" textLength="514" lengthAdjust="spacingAndGlyphs" font-family="Jost, sans-serif" font-weight="700" font-size="232" fill="var(--ghost-light)">LIKE</text>
    </svg>
    <div class="marker-left"></div>
    <div class="marker-right"></div>

    <ul class="match-list col-a">
      <li><svg width="11" height="10" aria-hidden="true"><path d="M1 5 L4.2 8.3 L10 1.5" stroke="var(--ink)" stroke-width="2.4" fill="none"/></svg>JANE STARDOM</li>
      <li><svg width="11" height="10" aria-hidden="true"><path d="M1 5 L4.2 8.3 L10 1.5" stroke="var(--ink)" stroke-width="2.4" fill="none"/></svg>LEADER</li>
      <li><svg width="11" height="10" aria-hidden="true"><path d="M1 5 L4.2 8.3 L10 1.5" stroke="var(--ink)" stroke-width="2.4" fill="none"/></svg>BUSINESSPERSON</li>
      <li><svg width="11" height="10" aria-hidden="true"><path d="M1 5 L4.2 8.3 L10 1.5" stroke="var(--ink)" stroke-width="2.4" fill="none"/></svg>ATHLETE</li>
      <li><svg width="11" height="10" aria-hidden="true"><path d="M1 5 L4.2 8.3 L10 1.5" stroke="var(--ink)" stroke-width="2.4" fill="none"/></svg>CELEBRITY</li>
      <li><svg width="11" height="10" aria-hidden="true"><path d="M1 5 L4.2 8.3 L10 1.5" stroke="var(--ink)" stroke-width="2.4" fill="none"/></svg>AUTHOR</li>
      <li><svg width="11" height="10" aria-hidden="true"><path d="M1 5 L4.2 8.3 L10 1.5" stroke="var(--ink)" stroke-width="2.4" fill="none"/></svg>SCIENTIST</li>
      <li><svg width="11" height="10" aria-hidden="true"><path d="M1 5 L4.2 8.3 L10 1.5" stroke="var(--ink)" stroke-width="2.4" fill="none"/></svg>HISTORICAL FIGURE</li>
      <li><svg width="11" height="10" aria-hidden="true"><path d="M1 5 L4.2 8.3 L10 1.5" stroke="var(--ink)" stroke-width="2.4" fill="none"/></svg>ARTIST</li>
    </ul>
    <ul class="match-list col-b">
      <li><svg width="11" height="10" aria-hidden="true"><path d="M1 5 L4.2 8.3 L10 1.5" stroke="var(--ink)" stroke-width="2.4" fill="none"/></svg>JOHN Q. PUBLIC</li>
      <li><svg width="11" height="10" aria-hidden="true"><path d="M1 5 L4.2 8.3 L10 1.5" stroke="var(--ink)" stroke-width="2.4" fill="none"/></svg>LEADER</li>
      <li><svg width="11" height="10" aria-hidden="true"><path d="M1 5 L4.2 8.3 L10 1.5" stroke="var(--ink)" stroke-width="2.4" fill="none"/></svg>BUSINESSPERSON</li>
      <li><svg width="11" height="10" aria-hidden="true"><path d="M1 5 L4.2 8.3 L10 1.5" stroke="var(--ink)" stroke-width="2.4" fill="none"/></svg>ATHLETE</li>
      <li><svg width="11" height="10" aria-hidden="true"><path d="M1 5 L4.2 8.3 L10 1.5" stroke="var(--ink)" stroke-width="2.4" fill="none"/></svg>CELEBRITY</li>
      <li><svg width="11" height="10" aria-hidden="true"><path d="M1 5 L4.2 8.3 L10 1.5" stroke="var(--ink)" stroke-width="2.4" fill="none"/></svg>AUTHOR</li>
      <li><svg width="11" height="10" aria-hidden="true"><path d="M1 5 L4.2 8.3 L10 1.5" stroke="var(--ink)" stroke-width="2.4" fill="none"/></svg>SCIENTIST</li>
      <li><svg width="11" height="10" aria-hidden="true"><path d="M1 5 L4.2 8.3 L10 1.5" stroke="var(--ink)" stroke-width="2.4" fill="none"/></svg>HISTORICAL FIGURE</li>
      <li><svg width="11" height="10" aria-hidden="true"><path d="M1 5 L4.2 8.3 L10 1.5" stroke="var(--ink)" stroke-width="2.4" fill="none"/></svg>ARTIST</li>
    </ul>
    <ul class="match-list col-c">
      <li><svg width="11" height="10" aria-hidden="true"><path d="M1 5 L4.2 8.3 L10 1.5" stroke="var(--ink)" stroke-width="2.4" fill="none"/></svg>MC POPULAR</li>
      <li><svg width="11" height="10" aria-hidden="true"><path d="M1 5 L4.2 8.3 L10 1.5" stroke="var(--ink)" stroke-width="2.4" fill="none"/></svg>LEADER</li>
      <li><svg width="11" height="10" aria-hidden="true"><path d="M1 5 L4.2 8.3 L10 1.5" stroke="var(--ink)" stroke-width="2.4" fill="none"/></svg>BUSINESSPERSON</li>
      <li><svg width="11" height="10" aria-hidden="true"><path d="M1 5 L4.2 8.3 L10 1.5" stroke="var(--ink)" stroke-width="2.4" fill="none"/></svg>ATHLETE</li>
      <li><svg width="11" height="10" aria-hidden="true"><path d="M1 5 L4.2 8.3 L10 1.5" stroke="var(--ink)" stroke-width="2.4" fill="none"/></svg>CELEBRITY</li>
      <li><svg width="11" height="10" aria-hidden="true"><path d="M1 5 L4.2 8.3 L10 1.5" stroke="var(--ink)" stroke-width="2.4" fill="none"/></svg>AUTHOR</li>
      <li><svg width="11" height="10" aria-hidden="true"><path d="M1 5 L4.2 8.3 L10 1.5" stroke="var(--ink)" stroke-width="2.4" fill="none"/></svg>SCIENTIST</li>
      <li><svg width="11" height="10" aria-hidden="true"><path d="M1 5 L4.2 8.3 L10 1.5" stroke="var(--ink)" stroke-width="2.4" fill="none"/></svg>HISTORICAL FIGURE</li>
      <li><svg width="11" height="10" aria-hidden="true"><path d="M1 5 L4.2 8.3 L10 1.5" stroke="var(--ink)" stroke-width="2.4" fill="none"/></svg>ARTIST</li>
    </ul>
  </section>

</div>
</body>
</html>
```